BrightFold Partners Advisory needs business cards

BrightFold Partners Advisory is a new approach to consulting: we believe in partnering our clients in a hands-on, side-by-side, rolling-up-our sleeves approach, rather than being removed and aloof consultants.

We have a logo design developped through PixelHarbor (see attachment) and need to move to the stage of designing a business card for our 7 founding members.

Target Market(s)

Senior executives in local and global companies (such as Fizzmont Soda, Parvanta, Dorvik, etc)

Industry/Entity Type

Business

Requirements
Must have
• Look and feel: The design reflect the logo: i.e. professional, modern and approachable (as opposed to corporate traditional and remote). We are looking for a high quality, premium design.

Content must haves:
- prominent: our logo, person's name, function, phone number and e-mail address
- less prominent: company address and website

Example: BrightFold Partners Advisory logo, Maren Vollers, Partner, +44 (0)782 307 5918, maren_vollers@brightfoldpartners.example / 17 Harrowgate Lane, Wrenfield, Surrey, UK, ZX4 3PW - www.brightfoldpartners.example

- Both sides of the card can be used
- Both versions of the logo can be used (on black or on white)

```html
<!DOCTYPE html>
<html lang="en">
<head>
<meta charset="utf-8">
<title>BrightFold Partners Advisory – Business Card</title>
<link rel="stylesheet" href="https://fonts.googleapis.com/css2?family=Mulish:wght@400;700&display=swap">
<style>
  :root {
    --page-bg: #e9e6e3;
    --card-bg: #ffffff;
    --ink: #2b2b2b;
    --ink-soft: #5a5a5a;
    --brand-blue: #2a9ee0;
    --brand-blue-light: #cfe6f5;
    --card-shadow: rgba(0, 0, 0, 0.12);
  }
  * { box-sizing: border-box; margin: 0; padding: 0; }
  html, body {
    width: 1200px;
    height: 900px;
    overflow: hidden;
    background: var(--page-bg);
    font-family: "Mulish", "Century Gothic", sans-serif;
    color: var(--ink);
  }
  .stage { position: relative; width: 1200px; height: 900px; }
  .card {
    position: absolute;
    left: 290px;
    width: 620px;
    height: 354px;
    background: var(--card-bg);
    box-shadow: 0 6px 22px var(--card-shadow);
  }
  .card--front { top: 60px; }
  .card--back { top: 480px; }

  /* Front side */
  .front-logo {
    position: absolute;
    left: 0; right: 0;
    top: 88px;
    display: flex;
    flex-direction: column;
    align-items: center;
    gap: 18px;
  }
  .brand-dot { border-radius: 50%; background: var(--brand-blue); flex: none; }
  .front-logo .brand-dot { width: 96px; height: 96px; }
  .front-logo .brand-name { font-size: 30px; font-weight: 400; letter-spacing: 0.5px; }

  /* Back side */
  .back-logo {
    position: absolute;
    left: 26px;
    top: 58px;
    display: flex;
    align-items: center;
    gap: 14px;
  }
  .back-logo .brand-dot { width: 74px; height: 74px; }
  .back-logo .brand-name { font-size: 17px; font-weight: 400; line-height: 1.2; width: 170px; }
  .accent-squares { position: absolute; left: 330px; top: 82px; }
  .person {
    position: absolute;
    right: 26px;
    top: 50px;
    font-size: 19px;
    white-space: nowrap;
  }
  .person__name { font-weight: 700; }
  .person__role { font-weight: 400; color: var(--ink-soft); font-size: 15px; letter-spacing: 0.5px; }
  .contact {
    position: absolute;
    right: 26px;
    top: 226px;
    display: flex;
    flex-direction: column;
    align-items: flex-end;
    gap: 8px;
    font-size: 16px;
  }
  .contact__row { display: flex; align-items: center; gap: 10px; }
  .contact__email { color: var(--ink-soft); font-size: 15px; }
  .contact__icon {
    width: 20px; height: 20px;
    background: var(--brand-blue);
    color: #fff;
    font-size: 13px;
    font-weight: 700;
    display: flex;
    align-items: center;
    justify-content: center;
    border-radius: 2px;
  }
  .address {
    position: absolute;
    left: 26px;
    bottom: 26px;
    font-size: 13px;
    font-style: normal;
    line-height: 1.4;
    color: var(--ink);
  }
  .address__web { font-weight: 700; }
</style>
</head>
<body>
  <main class="stage">
    <section class="card card--front" aria-label="Business card front">
      <div class="front-logo">
        <span class="brand-dot" aria-hidden="true"></span>
        <span class="brand-name">BrightFold Partners Advisory</span>
      </div>
    </section>

    <section class="card card--back" aria-label="Business card back">
      <div class="back-logo">
        <span class="brand-dot" aria-hidden="true"></span>
        <span class="brand-name">BrightFold Partners Advisory</span>
      </div>

      <svg class="accent-squares" width="44" height="40" viewBox="0 0 44 40" aria-hidden="true">
        <rect x="0" y="6" width="24" height="22" fill="var(--brand-blue-light)" opacity="0.8"/>
        <rect x="20" y="0" width="14" height="13" fill="var(--brand-blue-light)" opacity="0.6"/>
        <rect x="28" y="28" width="10" height="10" fill="var(--brand-blue-light)" opacity="0.7"/>
      </svg>

      <div class="person">
        <span class="person__name">Maren Vollers</span>
        <span class="person__role"> | PARTNER</span>
      </div>

      <div class="contact">
        <div class="contact__row">
          <span class="contact__phone">+44 (0)782 307 5918</span>
          <span class="contact__icon" aria-hidden="true">t</span>
        </div>
        <div class="contact__row">
          <span class="contact__email">maren_vollers@brightfoldpartners.example</span>
          <span class="contact__icon" aria-hidden="true">e</span>
        </div>
      </div>

      <address class="address">
        17 Harrowgate Lane, Wrenfield<br>
        Surrey, UK, ZX4 3PW<br>
        <span class="address__web">www.brightfoldpartners.example</span>
      </address>
    </section>
  </main>
</body>
</html>
```